13 Tovi - new website design project

Our company Tovi Electrical is developing a new lead generation website focused on Electrical, LED Lighting and Solar Power. We need a high converting website.

Example of our current website is www.tovielectrical.com.au You can take content from this website for this new design. Our colours are red, black and white. For our new website we would like to promote Tovi, Bright Days Ahead. Please listen to the jingle.

The below link is the company jingle that we have developed.
http://www.tunecraftstudio.com.au/tov-tc-v1/

The key for this brief is to generate leads for Electrical, LED Lighting (for commercial) and Solar Power & Storage.

Target Market(s)

Business owners in Melbourne Victoria

Number of Pages Required

4 page

Colors
ec1f27
ffffff

Requirements
Must have
• This page must be clean, be in line with company branding and a high converting lead website.

```html
<!DOCTYPE html>
<html lang="en">
<head>
<meta charset="utf-8">
<title>Tovi Electrical</title>
<link href="https://fonts.googleapis.com/css2?family=Roboto:wght@400;500;700&family=Open+Sans:wght@400;600;700&display=swap" rel="stylesheet">
<style>
:root{
  --red:#d42027;
  --red-dark:#b3161d;
  --ink:#2b2d35;
  --ink-soft:#3a3c45;
  --text:#444;
  --grey-bg:#f0f0f0;
  --line:#dcdcdc;
  --white:#fff;
}
*{box-sizing:border-box;margin:0;padding:0}
html,body{width:1200px;height:3711px;overflow:hidden}
body{position:relative;background:var(--white);font-family:'Open Sans',sans-serif;color:var(--text)}
.abs{position:absolute}
.section-title{position:absolute;left:0;width:1200px;text-align:center;font-family:'Roboto',sans-serif;font-weight:700;font-size:31px;color:var(--ink);text-transform:uppercase}
.section-title span{color:var(--red)}
.title-rule{position:absolute;width:56px;height:3px;background:var(--red)}
.btn-more{position:absolute;height:32px;width:158px;border-radius:16px;background:var(--red);color:#fff;font-family:'Roboto',sans-serif;font-weight:500;font-size:14px;line-height:32px;padding-left:24px;text-transform:uppercase}
.btn-more::after{content:"";position:absolute;right:3px;top:3px;width:26px;height:26px;border-radius:50%;background:var(--ink)}
.btn-more i{position:absolute;right:13px;top:12px;width:8px;height:8px;border-top:2px solid #fff;border-right:2px solid #fff;transform:rotate(45deg);z-index:1}
.arrow-dot{position:absolute;width:26px;height:26px;border-radius:50%;background:var(--red)}
.arrow-dot.dark{background:var(--ink)}
.arrow-dot::after{content:"";position:absolute;left:7px;top:9px;width:7px;height:7px;border-top:2px solid #fff;border-right:2px solid #fff;transform:rotate(45deg)}

/* header */
.logo{position:absolute;left:82px;top:22px;display:flex;align-items:center;gap:10px}
.logo-mark{width:40px;height:40px;border-radius:50%;background:var(--red)}
.logo-name{font-family:'Roboto',sans-serif;font-weight:700;font-size:40px;color:var(--ink);line-height:1}
.logo-tag{position:absolute;left:82px;top:74px;font-family:'Roboto',sans-serif;font-weight:500;font-size:15px;color:var(--ink)}
.top-contact{position:absolute;top:22px;height:30px;display:flex;align-items:center;font-size:14px;color:var(--ink)}
.ring-icon{width:30px;height:30px;border-radius:50%;border:2px solid var(--red);margin-right:10px;display:flex;align-items:center;justify-content:center}
.social{position:absolute;display:flex;gap:8px}
.social span{width:32px;height:32px;border-radius:50%;background:var(--red)}
.main-nav{position:absolute;left:359px;top:82px;width:841px;height:47px;background:var(--ink)}
.main-nav ul{list-style:none;display:flex;height:100%;align-items:center}
.main-nav li{font-family:'Roboto',sans-serif;font-weight:500;font-size:15px;color:#fff;text-transform:uppercase;text-align:center;border-right:1px solid #4a4c55;height:47px;line-height:47px}
.main-nav li.active span{background:var(--red);border-radius:16px;padding:7px 24px}
.header-rule{position:absolute;left:0;top:127px;width:1200px;height:3px;background:var(--red)}

/* hero */
.hero{position:absolute;left:0;top:130px;width:1200px;height:590px;background:linear-gradient(160deg,#c9c9d6 0%,#eceef4 35%,#b7b4c8 60%,#8d8a9a 100%)}
.hero-badge{position:absolute;left:75px;top:63px;width:370px;height:370px;border-radius:50%;background:rgba(40,42,50,.78)}
.hero-badge h1{position:absolute;left:20px;top:160px;width:330px;text-align:center;font-family:'Roboto',sans-serif;font-weight:500;font-size:29px;line-height:40px;color:#fff}
.hero-dots{position:absolute;left:162px;top:442px;display:flex;gap:6px}
.hero-dots span{width:11px;height:11px;border-radius:50%;background:#ddd}
.hero-dots span.on{background:var(--red)}

/* services */
.service-card{position:absolute;top:858px;width:327px;height:258px}
.service-card h3{height:74px;background:var(--ink);border-radius:8px 8px 0 0;color:#fff;font-family:'Roboto',sans-serif;font-weight:500;font-size:21px;text-transform:uppercase;text-align:center;line-height:74px}
.service-photo{height:184px}

/* about */
.about-photo{position:absolute;left:0;top:1197px;width:599px;height:456px;background:linear-gradient(180deg,#9aa1a8 0%,#c9ced2 45%,#7d8389 100%)}
.about-panel{position:absolute;left:599px;top:1197px;width:601px;height:456px;background:var(--grey-bg)}
.about-panel h2{position:absolute;left:39px;top:56px;font-family:'Roboto',sans-serif;font-weight:700;font-size:31px;color:var(--ink);text-transform:uppercase}
.about-panel h2 span{color:var(--red)}
.about-panel p{position:absolute;left:39px;width:525px;font-size:14px;line-height:22px;text-align:justify;color:#555}

/* why */
.why-item{position:absolute;width:300px;text-align:center}
.why-item h4{font-family:'Roboto',sans-serif;font-weight:700;font-size:19px;color:var(--ink);margin-bottom:8px}
.why-item p{font-size:13px;line-height:19px;color:#555}

/* work */
.work-bg{position:absolute;left:0;top:2405px;width:1200px;height:668px;background:var(--grey-bg)}
.work-card{position:absolute;top:2563px;width:327px;height:401px;background:#fff;border:1px solid var(--line)}
.work-brand{height:64px;display:flex;align-items:center;justify-content:center;font-family:'Roboto',sans-serif;font-weight:700;font-size:30px;color:var(--ink)}
.work-photo{height:149px;position:relative}
.zoom{position:absolute;right:8px;bottom:8px;width:34px;height:34px;border-radius:50%;background:#555;border:2px solid #fff}
.work-card h5{margin:22px 12px 0;font-family:'Roboto',sans-serif;font-weight:700;font-size:17px;color:var(--ink)}
.work-card .role{margin:4px 12px 0;font-size:13px;color:#555}
.work-card p.quote{margin:8px 12px 0;font-size:13.5px;line-height:21px;color:#444}
.work-dots{position:absolute;left:573px;top:3000px;display:flex;gap:6px}
.work-dots span{width:12px;height:12px;border-radius:50%;background:var(--ink)}
.work-dots span.on{background:var(--red)}

/* clients */
.client{position:absolute;top:3211px;width:213px;height:97px;display:flex;align-items:center;justify-content:center;font-family:'Roboto',sans-serif;font-weight:700;font-size:25px;text-align:center}

/* footer */
.footer{position:absolute;left:0;top:3370px;width:1200px;height:297px;background:var(--ink);color:#ddd}
.footer h6{position:absolute;top:52px;font-family:'Roboto',sans-serif;font-weight:700;font-size:16px;color:#fff;text-transform:uppercase}
.footer h6 span{color:var(--red)}
.f-divider{position:absolute;top:44px;width:1px;height:200px;background:#474954}
.quick-links{position:absolute;left:82px;top:94px;list-style:none;font-size:13px;line-height:32px}
.quick-links li::before{content:"• ";color:#aaa}
.quick-links li.current{color:var(--red)}
.f-contact{position:absolute;left:287px;font-size:13.5px;line-height:20px;padding-left:26px}
.f-contact::before{content:"";position:absolute;left:0;top:3px;width:12px;height:12px;border-radius:50%;background:var(--red)}
.f-field{position:absolute;left:606px;width:268px;height:34px;border:1px solid #888;color:#ddd;font-size:13px;line-height:32px;padding-left:8px}
.f-submit{position:absolute;left:606px;top:219px;width:100px;height:28px;border-radius:14px;background:var(--red);color:#fff;font-family:'Roboto',sans-serif;font-weight:500;font-size:12px;line-height:28px;padding-left:20px}
.f-submit::after{content:"";position:absolute;right:12px;top:10px;width:6px;height:6px;border-top:2px solid #fff;border-right:2px solid #fff;transform:rotate(45deg)}
.copy-bar{position:absolute;left:0;top:3667px;width:1200px;height:44px;background:var(--red);color:#fff;font-size:13px;line-height:44px}
</style>
</head>
<body>

<header>
  <div class="logo"><span class="logo-mark"></span><span class="logo-name">TOVI</span></div>
  <div class="logo-tag">Bright Days Ahead</div>

  <div class="top-contact" style="left:676px">
    <span class="ring-icon"><svg width="14" height="14" viewBox="0 0 24 24"><path d="M6.6 10.8a15 15 0 0 0 6.6 6.6l2.2-2.2a1 1 0 0 1 1-.25 11.4 11.4 0 0 0 3.6.6 1 1 0 0 1 1 1V20a1 1 0 0 1-1 1A17 17 0 0 1 3 4a1 1 0 0 1 1-1h3.5a1 1 0 0 1 1 1c0 1.25.2 2.45.6 3.6a1 1 0 0 1-.25 1z" fill="#d42027"/></svg></span>138574
  </div>
  <div class="top-contact" style="left:784px">
    <span class="ring-icon"><svg width="14" height="12" viewBox="0 0 24 18"><rect x="1" y="1" width="22" height="16" rx="2" fill="none" stroke="#d42027" stroke-width="2.4"/><path d="M2 2l10 8 10-8" fill="none" stroke="#d42027" stroke-width="2.4"/></svg></span>service@tovielectrical.com.au
  </div>
  <div class="social" style="left:1014px;top:21px"><span></span><span></span><span></span></div>

  <nav class="main-nav">
    <ul>
      <li class="active" style="width:150px;border:none"><span>Home</span></li>
      <li style="width:150px">Tovi Story</li>
      <li style="width:150px">Services</li>
      <li style="width:160px">Our Work</li>
      <li style="width:180px;border:none">Contact Us</li>
    </ul>
  </nav>
  <div class="header-rule"></div>
</header>

<section class="hero" role="img" aria-label="Bright modern office reception with curved ceiling and violet lighting">
  <div class="hero-badge">
    <h1>Australia's largest fully integrated Electrical &amp; Energy Solutions Provider.</h1>
  </div>
  <div class="hero-dots"><span class="on"></span><span></span><span></span></div>
</section>

<section class="services">
  <h2 class="section-title" style="top:760px">Our <span>Services</span></h2>
  <div class="title-rule" style="left:572px;top:810px"></div>

  <div class="service-card" style="left:82px">
    <h3>Electrical</h3>
    <div class="service-photo" role="img" aria-label="Electrician in a hard hat wiring a switchboard" style="background:linear-gradient(135deg,#4a6a9a,#c8b24a 45%,#7a8aa0)"></div>
  </div>
  <div class="btn-more" style="left:166px;top:1100px">Read more<i></i></div>

  <div class="service-card" style="left:435px">
    <h3>LED Lighting</h3>
    <div class="service-photo" role="img" aria-label="Several LED light bulbs on a white surface" style="background:linear-gradient(135deg,#e4e4e4,#bfbfbf 50%,#ededed)"></div>
  </div>
  <div class="btn-more" style="left:519px;top:1100px">Read more<i></i></div>

  <div class="service-card" style="left:794px">
    <h3>Solar Power</h3>
    <div class="service-photo" role="img" aria-label="Installers fitting solar panels on a roof" style="background:linear-gradient(160deg,#8a5a3a,#3d6ab0 40%,#2a4e8c)"></div>
  </div>
  <div class="btn-more" style="left:878px;top:1100px">Read more<i></i></div>
</section>

<section class="about">
  <div class="about-photo" role="img" aria-label="Large bright warehouse interior with high ceiling lights"></div>
  <div class="about-panel">
    <h2>About <span>Tovi</span></h2>
    <div class="title-rule" style="left:39px;top:107px"></div>
    <p style="top:133px">Tovi Electrical was formed to be an expert Electricity Contracting Company providing services to all Residential and Commercial Customers. With over 10 years of experience, Tovi Electrical has developed a highly-experienced team of professionals that ensure all our customer expectations are met.</p>
    <p style="top:245px">Lorem ipsum dolor sit amet, consectetuer adipiscing elit, sed diam nonummy nibh euismod tincidunt ut laoreet dolore magna aliquam erat volutpat. Ut wisi enim ad minim veniam.</p>
    <div class="btn-more" style="left:39px;top:359px">Read more<i></i></div>
  </div>
</section>

<section class="why">
  <h2 class="section-title" style="top:1693px">Why <span>Choose Us?</span></h2>
  <div class="title-rule" style="left:572px;top:1743px"></div>

  <div class="why-item" style="left:60px;top:1796px">
    <h4>Professional Service</h4>
    <p>When you hire a Tovi Electrical Electrician you will get a professional and well-presented Electrician that comes skilled and ready to do the job.</p>
  </div>
  <div class="arrow-dot" style="left:197px;top:1914px"></div>

  <div class="why-item" style="left:444px;top:1796px">
    <h4>Value for Money</h4>
    <p>We provide extremely competitive pricing, which means you get value for money on quality that is comparable to the best in the industry.</p>
  </div>
  <div class="arrow-dot" style="left:581px;top:1914px"></div>

  <div class="why-item" style="left:840px;top:1796px">
    <h4>Fully insured</h4>
    <p>Tovi Electrical is fully insured and equipped to handle break downs and service call outs.</p>
  </div>
  <div class="arrow-dot" style="left:977px;top:1914px"></div>

  <svg class="abs" style="left:0;top:1920px" width="1200" height="270" viewBox="0 0 1200 270">
    <g fill="none" stroke-width="40">
      <path d="M82 133 H111 A99 99 0 0 0 309 133" stroke="#d42027"/>
      <path d="M297 133 A99 99 0 0 1 495 133" stroke="#2b2d35"/>
      <path d="M495 133 A99 99 0 0 0 693 133" stroke="#d42027"/>
      <path d="M693 133 A99 99 0 0 1 891 133" stroke="#2b2d35"/>
      <path d="M891 133 A99 99 0 0 0 1089 133 H1118" stroke="#d42027"/>
    </g>
    <g fill="#fff" stroke="#d9d9d9" stroke-width="4">
      <circle cx="210" cy="133" r="78"/>
      <circle cx="396" cy="133" r="78"/>
      <circle cx="594" cy="133" r="78"/>
      <circle cx="792" cy="133" r="78"/>
      <circle cx="990" cy="133" r="78"/>
    </g>
    <g fill="#2b2d35">
      <circle cx="205" cy="118" r="13"/>
      <path d="M182 158 a23 23 0 0 1 46 0z"/>
      <circle cx="228" cy="150" r="9"/>
      <circle cx="228" cy="150" r="4" fill="#fff"/>
      <circle cx="396" cy="125" r="24"/>
      <path d="M396 110 l4.5 9 10 1.5 -7.2 7 1.7 10 -9 -4.7 -9 4.7 1.7 -10 -7.2 -7 10 -1.5z" fill="#fff"/>
      <path d="M382 145 l-8 22 10 -3 6 8 6 -20z M410 145 l8 22 -10 -3 -6 8 -6 -20z"/>
      <path d="M584 100 h20 l-6 10 q24 14 20 38 q-4 14 -24 14 q-20 0 -24 -14 q-4 -24 20 -38z"/>
      <text x="594" y="150" font-family="Roboto,sans-serif" font-weight="700" font-size="26" fill="#fff" text-anchor="middle">$</text>
      <circle cx="792" cy="133" r="26"/>
      <path d="M770 133 h44 M792 107 v52 M779 112 q-12 21 0 42 M805 112 q12 21 0 42" stroke="#fff" stroke-width="3" fill="none"/>
      <path d="M990 103 l26 10 v18 q0 22 -26 34 q-26 -12 -26 -34 v-18z"/>
      <path d="M978 134 l9 9 16 -17" stroke="#fff" stroke-width="5" fill="none"/>
    </g>
  </svg>

  <div class="why-item" style="left:246px;top:2187px">
    <h4>5 year workmanship guarantee</h4>
    <p>You can buy with confidence as all of our work has a 5 year workmanship guarantee. For your peace of mind, we unconditionally back our electrical work. We will come back to fix any problems at our own expense.</p>
  </div>
  <div class="arrow-dot dark" style="left:383px;top:2327px"></div>

  <div class="why-item" style="left:642px;top:2187px">
    <h4>Environmentally friendly</h4>
    <p>We a committed to reducing carbon emissions by installing Solar Power and upgrading sites to LED Lighting. In addition to reducing the carbon emissions we recycle Fluorescent Tubes, Highbay Globes, Metal and Cardboard.</p>
  </div>
  <div class="arrow-dot dark" style="left:779px;top:2327px"></div>
</section>

<section class="work">
  <div class="work-bg"></div>
  <h2 class="section-title" style="top:2455px">Our <span>Work</span></h2>
  <div class="title-rule" style="left:572px;top:2505px"></div>

  <article class="work-card" style="left:82px">
    <div class="work-brand" style="background:#f4e31a">Outback Supply Co</div>
    <div class="work-photo" role="img" aria-label="Outdoor store front with shoppers" style="background:linear-gradient(180deg,#6c6c6c,#a7a39a 60%,#585858)"><span class="zoom"></span></div>
    <h5>Jordan Pellow</h5>
    <div class="role">Executive Outback Supply Co</div>
    <p class="quote">The service, communication and after sales service of Tovi Electrical has been awesome. We would strongly recommend them to any business contemplating upgrading.</p>
  </article>

  <article class="work-card" style="left:435px">
    <div class="work-brand" style="color:#d42027">Brightmart</div>
    <div class="work-photo" role="img" aria-label="Brightly lit retail shop interior" style="background:linear-gradient(180deg,#a8a8b0,#d6c8c8 50%,#9a7070)"><span class="zoom"></span></div>
    <h5>R. Marlo</h5>
    <div class="role">Balwyn North VIC</div>
    <p class="quote">They clean up after the job, explained everything I needed to know and answered all questions, very professional. Will use them again in the future!</p>
  </article>

  <article class="work-card" style="left:794px">
    <div class="work-brand" style="color:#1d5fa8">Nordalloy</div>
    <div class="work-photo" role="img" aria-label="Industrial steel warehouse interior" style="background:linear-gradient(180deg,#5d6670,#9aa3ab 55%,#4c545c)"><span class="zoom"></span></div>
    <h5>Dellan</h5>
    <div class="role">Cranbourne North VIC</div>
    <p class="quote">Excellent work and very professional. Marcus takes time to explain everything and demonstrate workings. Very clear precise and accurate.</p>
  </article>

  <div class="work-dots"><span class="on"></span><span></span><span></span></div>
</section>

<section class="clients">
  <h2 class="section-title" style="top:3108px">Our Satisfied <span>Clients</span></h2>
  <div class="title-rule" style="left:572px;top:3158px"></div>
  <div class="client" style="left:129px;background:#fff;border:1px solid #eee;color:#d42027">Brightmart</div>
  <div class="client" style="left:371px;background:#f4e31a;color:#2b2d35">Outback Supply Co</div>
  <div class="client" style="left:614px;background:#d42027;color:#fff;font-size:22px">Heron Plumbing Supplies</div>
  <div class="client" style="left:856px;background:#c8161d;color:#fff">Golden Grill</div>
</section>

<footer class="footer">
  <h6 style="left:82px">Quick <span>Links</span></h6>
  <ul class="quick-links">
    <li class="current">Home</li>
    <li>Tovi Story</li>
    <li>Services</li>
    <li>Our Work</li>
    <li>Contact Us</li>
  </ul>
  <div class="f-divider" style="left:240px"></div>

  <h6 style="left:287px">Contact <span>Details</span></h6>
  <div class="f-contact" style="top:94px"><strong style="color:#fff">Tovi</strong><br>22/48 Larkin Rd, Glen Ashby,<br>VIC 3160</div>
  <div class="f-contact" style="top:174px">138574</div>
  <div class="f-contact" style="top:214px">service@tovielectrical.com.au</div>
  <div class="f-divider" style="left:560px"></div>

  <h6 style="left:606px">Quick <span>Inquiry</span></h6>
  <div class="f-field" style="top:92px">Name</div>
  <div class="f-field" style="top:132px">Email</div>
  <div class="f-field" style="top:172px">Message</div>
  <div class="f-submit">SUBMIT</div>
  <div class="f-divider" style="left:920px"></div>

  <div class="abs" style="left:968px;top:118px;display:flex;align-items:center;gap:8px">
    <span style="width:34px;height:34px;border-radius:50%;background:var(--red)"></span>
    <span style="font-family:'Roboto',sans-serif;font-weight:700;font-size:38px;color:#fff;line-height:1">TOVI</span>
  </div>
  <div class="abs" style="left:968px;top:166px;font-family:'Roboto',sans-serif;font-weight:500;font-size:14px;color:#fff">Bright Days Ahead</div>
  <div class="social" style="left:990px;top:200px"><span></span><span></span><span></span></div>
</footer>

<div class="copy-bar">
  <span class="abs" style="left:82px">Copyright © 2017 Tovi. All Right Reserved.</span>
  <span class="abs" style="left:926px">Terms and Conditions &nbsp;|&nbsp; Privacy</span>
</div>

</body>
</html>
```